custom carpentry, woodworking and home repair company needs logo design and business card design

Attention: I apologize but I just received notification from my state that I cannot use the company name that I originally submitted (Beyond The Bench). The new name will be Joinolux We need a company logo and business card design for our new company based in the Hampton Roads area of Virginia. The company name is Joinolux. The final design should give a first impression of true craftsmanship and attention to detail. We would like the card to include the company name, my name Mark Tellman (owner), phone number (757) 348-2615, website (joinolux-example.com) and email address (mark@joinolux-example.com). Everything else is up to your discretion. Thanks, have fun, and good luck.

Industry/Entity Type

Business

Contact Information for Business Card

See project description

Logo Text

see project description

Colors

Designer to choose colors to be used in the design.

```html
<!DOCTYPE html>
<html lang="en">
<head>
<meta charset="utf-8">
<title>Joinolux Business Card</title>
<link rel="stylesheet" href="https://fonts.googleapis.com/css2?family=Oswald:wght@500;700&family=Roboto+Condensed:wght@400;700&display=swap">
<style>
  :root {
    --backdrop: #1c1c1c;
    --wood-light: #f6c27a;
    --wood-mid: #eda95a;
    --wood-deep: #e09145;
    --birch-light: #f7f5f0;
    --birch-mid: #e9e6df;
    --ink-black: #1a1410;
    --green-dark: #1d6b2c;
    --green-mid: #2e8b3a;
    --green-light: #5cb845;
    --rule-grey: #8f8a80;
  }
  * { margin: 0; padding: 0; box-sizing: border-box; }
  html, body { width: 1200px; height: 873px; overflow: hidden; }
  body {
    background: var(--backdrop);
    display: flex;
    align-items: center;
    justify-content: center;
    gap: 80px;
    font-family: "Roboto Condensed", "Arial Narrow", sans-serif;
  }
  .card {
    position: relative;
    width: 330px;
    height: 560px;
    border-radius: 16px;
    overflow: hidden;
    box-shadow: 0 10px 30px rgba(0,0,0,.5);
  }
  .card-surface {
    position: absolute;
    inset: 0;
  }
  .card-front .card-surface {
    background: linear-gradient(160deg, var(--wood-light) 0%, var(--wood-mid) 55%, var(--wood-deep) 100%);
  }
  .card-back .card-surface {
    background: linear-gradient(160deg, var(--birch-light) 0%, var(--birch-mid) 100%);
  }
  .card-content {
    position: relative;
    height: 100%;
    display: flex;
    flex-direction: column;
    align-items: center;
  }
  .brand {
    display: flex;
    align-items: center;
    gap: 10px;
    font-family: "Oswald", "Arial Narrow", sans-serif;
    font-weight: 700;
    font-size: 40px;
    letter-spacing: 1px;
    text-transform: uppercase;
    line-height: 1;
  }
  .brand-dot {
    width: 14px;
    height: 14px;
    border-radius: 50%;
  }
  .card-front .brand { color: var(--ink-black); margin-top: 200px; }
  .card-front .brand-dot { background: var(--ink-black); }
  .card-front .website {
    margin-top: auto;
    margin-bottom: 48px;
    font-weight: 700;
    font-size: 15px;
    letter-spacing: .5px;
    text-transform: uppercase;
    color: var(--ink-black);
  }
  .card-back .brand { color: var(--green-dark); margin-top: 70px; }
  .card-back .brand-dot { background: var(--green-light); }
  .divider {
    width: 170px;
    height: 2px;
    background: var(--rule-grey);
    opacity: .6;
  }
  .divider-top { margin-top: 44px; }
  .person { margin: 26px 0; text-align: center; }
  .person-name {
    font-family: "Oswald", "Arial Narrow", sans-serif;
    font-weight: 700;
    font-size: 28px;
    letter-spacing: .5px;
    text-transform: uppercase;
    color: var(--green-dark);
  }
  .person-role {
    font-weight: 700;
    font-size: 16px;
    text-transform: uppercase;
    color: var(--green-light);
    margin-top: 2px;
  }
  .divider-dotted { position: relative; }
  .divider-dotted::after {
    content: "";
    position: absolute;
    left: 50%;
    top: 50%;
    width: 8px;
    height: 8px;
    border-radius: 50%;
    background: var(--green-dark);
    transform: translate(-50%, -50%);
  }
  .contact {
    list-style: none;
    margin-top: 26px;
    text-align: center;
    font-size: 18px;
    line-height: 1.55;
    color: var(--green-dark);
  }
</style>
</head>
<body>
  <section class="card card-front">
    <div class="card-surface" role="img" aria-label="Warm maple wood grain texture"></div>
    <div class="card-content">
      <div class="brand"><span>Joinolux</span><span class="brand-dot"></span></div>
      <p class="website">www.joinolux-example.com</p>
    </div>
  </section>

  <section class="card card-back">
    <div class="card-surface" role="img" aria-label="Pale whitewashed wood grain texture"></div>
    <div class="card-content">
      <div class="brand"><span>Joinolux</span><span class="brand-dot"></span></div>
      <div class="divider divider-top"></div>
      <div class="person">
        <p class="person-name">Mark Tellman</p>
        <p class="person-role">Owner</p>
      </div>
      <div class="divider divider-dotted"></div>
      <ul class="contact">
        <li>(757) 348-2615</li>
        <li>mark@joinolux-example.com</li>
        <li>joinolux-example.com</li>
      </ul>
    </div>
  </section>
</body>
</html>
```